Beauty Page

**UPDATED Brief**
We are looking for a website for a beauty organisation that targets both MEN & WOMAN. The focus of the company is in four main areas:

- Health
* Naturopathy & Remedial Massage
- Body
* Yoga
* Personal Training
* Massage
- Skin
* Skin care products such as Velmoracine
- Beauty
* Waxing
* Eye Treatments

We have attached the logo, (a sample of the website that I did - based on the book) and the sample of the pdf book
Updates

Dear All,

Thank you for your patience regarding the beauty contest. We were not happy with the designs that were submitted to us. We therefore had the Graphic designer to do the pricelist book to get all the colours for the organisation.

We are now happy to relaunch the contest and invite you all to take a look at the brief, download a sample of the book and the website we designed on what I’m looking for (the website is only a draft so I don’t want you to copy it) and let your creative mind go wild and present some suggestions to us.

Thanks

 

Target Market(s)

Woman & Men age 24 - 60

Industry/Entity Type

It Company

Requirements
Must have
• Use of main colours
Black
White
Gray - (CYMK - 65, 58, 57, 37)
Purpleish - Maroon (CYMK - 52, 69, 47, 25)

Use of the three color dots on the page.
(white, maroon & Gray)
Same fonts as the book
- Helvetica LT Std
Should not have
• Logo must not be altered i.e different colours, fonts, shadows etc...

```html
<!DOCTYPE html>
<html lang="en">
<head>
<meta charset="utf-8">
<title>Lumaforme &amp; Beauty</title>
<link href="https://fonts.googleapis.com/css2?family=Arimo:wght@400;700&display=swap" rel="stylesheet">
<style>
:root{
  --purple-deep:#4a1458;
  --purple:#7b2a8a;
  --magenta:#a3339d;
  --lavender:#e6d8ee;
  --gray:#5d5b5c;
  --gray-light:#d9d6da;
  --black:#111;
  --white:#fff;
}
*{margin:0;padding:0;box-sizing:border-box}
html,body{width:876px;height:1200px;overflow:hidden}
body{font-family:"Arimo",Helvetica,Arial,sans-serif;color:var(--gray);
  background:radial-gradient(ellipse 520px 200px at 560px 60px,#c98fd6 0%,rgba(201,143,214,0) 70%),
  linear-gradient(180deg,#efe4f3 0%,#f8f4fa 30%,#f2edf4 100%);position:relative}
.abs{position:absolute}
.account-bar{left:440px;top:0;width:436px;height:24px;background:var(--black);color:#ccc;font-size:9px;display:flex;align-items:center;justify-content:space-around;text-transform:uppercase;letter-spacing:.3px}
.account-bar b{color:var(--white)}
.brand{left:30px;top:22px;color:var(--purple-deep);font-weight:700;font-size:40px;line-height:1;letter-spacing:-1px;display:flex;align-items:center;gap:12px}
.brand .dot{width:18px;height:18px;border-radius:50%;background:var(--magenta)}
.brand small{display:block;font-size:26px;letter-spacing:0;margin-top:4px}
.guarantee{left:672px;top:34px;width:188px;height:84px;background:linear-gradient(160deg,var(--magenta),var(--purple-deep));border-radius:6px;color:var(--white);text-align:center;padding-top:10px;font-weight:700;font-size:24px;line-height:1.05}
.guarantee span{display:block;font-size:14px;font-weight:400}
.guarantee em{display:inline-block;font-style:normal;background:var(--white);color:var(--purple-deep);font-size:11px;padding:1px 6px;margin-top:3px}
.main-nav{left:30px;top:125px;width:816px;height:44px;background:linear-gradient(180deg,#8c3a98,var(--purple-deep));display:flex;border-radius:3px;overflow:hidden}
.main-nav a{color:var(--white);text-decoration:none;font-size:14px;font-weight:700;display:flex;align-items:center;justify-content:center;border-right:1px solid rgba(255,255,255,.25)}
.main-nav a.active{background:linear-gradient(180deg,#c45ec8,var(--magenta))}
.hero{left:30px;top:180px;width:816px;height:320px;border:5px solid var(--white);box-shadow:0 1px 4px rgba(0,0,0,.2);background:linear-gradient(100deg,#d9c7c2 0%,#efe6ea 35%,#c9a6d4 70%,#8c4f9c 100%)}
.hero-caption{right:0;bottom:30px;width:440px;height:40px;background:linear-gradient(90deg,rgba(123,42,138,0),var(--purple));color:var(--white);font-size:20px;display:flex;align-items:center;justify-content:flex-end;padding-right:18px}
.card{background:var(--white);border:1px solid var(--gray-light);box-shadow:0 1px 3px rgba(0,0,0,.12)}
.card h3{font-size:12px;color:var(--gray);font-weight:400;line-height:1.2}
.card h2{font-size:18px;color:var(--purple);font-weight:700;line-height:1.1}
.card p{font-size:9.5px;line-height:1.4}
.ph{border-radius:2px}
.btn{background:linear-gradient(180deg,#9a4ba6,var(--purple-deep));color:var(--white);font-size:11px;font-weight:700;padding:6px 18px;border-radius:4px}
.section-title{font-size:26px;color:var(--purple);font-weight:400}
.sponsor-name{font-size:20px;font-weight:700;color:var(--black)}
.footer{left:20px;top:1062px;width:836px;height:122px;background:linear-gradient(180deg,#8c3a98,var(--purple-deep));border-radius:4px;color:var(--white)}
.footer ul{list-style:none;font-size:9.5px;line-height:1.65}
.footer li::before{content:"• ";color:#d9a7e0}
</style>
</head>
<body>

<div class="abs account-bar"><span>Your cart is empty</span><span>Currency | <b>USD</b></span><span><b>Checkout now ›</b></span><span>My account ▾</span></div>

<div class="abs brand"><div class="dot"></div><div>LUMAFORME<small>&amp; Beauty</small></div></div>

<div class="abs guarantee">60 DAYS<span>Money Back</span><em>GUARANTEE</em></div>

<nav class="abs main-nav">
  <a class="active" href="#" style="width:150px">HOME</a>
  <a href="#" style="width:190px">ABOUT US</a>
  <a href="#" style="width:270px">SERVICES &amp; TREATMENTS</a>
  <a href="#" style="width:206px;border-right:0">CONTACT US</a>
</nav>

<section class="abs hero" role="img" aria-label="Woman applying makeup with a brush">
  <div class="abs hero-caption">Health, Body &amp; Skin Care Center</div>
</section>

<div class="abs card" style="left:30px;top:512px;width:276px;height:262px;padding:12px">
  <h3>Welcome To</h3><h2>LUMAFORME &amp; BEAUTY</h2>
  <div class="ph" role="img" aria-label="Smiling woman portrait" style="margin-top:8px;height:118px;background:linear-gradient(120deg,#e7d6cf,#b9a3bc)"></div>
  <p style="margin-top:8px">Lumaforme &amp; Beauty is a health, massage, skincare centre that provides quality treatments and education to each and every client to cater for all individuals.</p>
</div>

<div class="abs card" style="left:315px;top:512px;width:285px;height:262px;padding:12px">
  <h3>Introducing</h3><h2>LUMAFORME &amp; BEAUTY</h2>
  <div class="ph" role="img" aria-label="Skin care product jars and tubes" style="margin-top:10px;height:150px;background:linear-gradient(180deg,#fff,#dfe6f0 60%,#b8c3d6)"></div>
  <div style="margin-top:10px;background:linear-gradient(90deg,var(--purple-deep),var(--magenta));color:#fff;font-size:10px;padding:6px 10px;border-radius:3px">Explore The Range of Beauty Products ›</div>
</div>

<div class="abs" style="left:607px;top:512px;width:239px;height:262px">
  <div style="font-size:12px;color:var(--purple);font-weight:700;margin:4px 0 6px">REVOLUTIONARY NEW TREATMENTS</div>
  <div class="ph" role="img" aria-label="Treatment video preview" style="height:190px;background:linear-gradient(180deg,#2a2a2a,#555)"></div>
  <svg width="239" height="26" viewBox="0 0 239 26" style="display:block">
    <rect width="239" height="26" fill="#e5e5e5"/>
    <polygon points="8,7 8,19 18,13" fill="#333"/>
    <rect x="26" y="11" width="150" height="4" fill="#bbb"/><rect x="26" y="11" width="12" height="4" fill="#c00"/>
    <rect x="186" y="8" width="10" height="10" fill="#555"/><rect x="206" y="8" width="22" height="10" fill="#555"/>
  </svg>
</div>

<div class="abs card" style="left:30px;top:783px;width:394px;height:260px;padding:12px 14px">
  <div class="section-title">Fresh Begin</div>
  <div class="abs ph" role="img" aria-label="Cleansing product bottles" style="left:14px;top:50px;width:190px;height:196px;background:linear-gradient(180deg,#f4f7ec,#cfe39d 60%,#8fc14a)"></div>
  <p class="abs" style="left:216px;top:110px;width:164px">Trust Fresh Begin by Velmoracine to do good things for your skin with cleansing, soothing, refreshing ingredients that feel and smell great.</p>
  <div class="abs btn" style="right:14px;bottom:14px">More INFO</div>
</div>

<div class="abs card" style="left:438px;top:783px;width:408px;height:260px;padding:12px 14px">
  <div style="font-size:13px;color:var(--gray)">Brands</div>
  <div class="section-title" style="line-height:1">Sponsors &amp; News</div>
  <div class="abs sponsor-name" style="left:14px;top:72px">Velmoracine</div>
  <div class="abs sponsor-name" style="left:14px;top:110px">Aurelite Studio</div>
  <div class="abs ph" role="img" aria-label="Botanic skin peel product banner" style="left:14px;top:150px;width:230px;height:94px;background:linear-gradient(180deg,#f2f6ec,#b9d59a)"></div>
  <div class="abs btn" style="right:14px;bottom:14px">Read MORE</div>
</div>

<footer class="abs footer">
  <div class="abs" style="left:20px;top:22px;font-weight:700;font-size:30px;line-height:1;letter-spacing:-1px">LUMAFORME<div style="font-size:20px;letter-spacing:0;margin-top:4px">&amp; Beauty</div></div>
  <ul class="abs" style="left:240px;top:20px"><li>Home</li><li>Beauty Range</li><li>Your Skin Type</li><li>FAQ's</li></ul>
  <ul class="abs" style="left:355px;top:20px"><li>Promotions</li><li>Benefits</li><li>Become a Stockist</li><li>Newsletter</li></ul>
  <ul class="abs" style="left:480px;top:20px"><li>Company</li><li>News</li><li>Media</li><li>Contact Us</li></ul>
  <ul class="abs" style="left:590px;top:20px"><li>Help</li><li>Terms &amp; Conditions</li><li>Privacy Policy</li><li>Disclaimer</li></ul>
  <div class="abs" style="left:716px;top:22px;font-size:11px;font-weight:700;text-align:center;width:110px;white-space:nowrap">Become a friend!
    <div style="width:34px;height:34px;background:var(--white);border-radius:4px;margin:10px auto 0"></div>
  </div>
</footer>

</body>
</html>
```